Lip Balm Label Design

Design a label for a Lavender-Mint lip balm. We make high-quality natural essential oil products. Please use the old label as an example of what exists. The label should include purple. The final design should be eye-catching and distinct. The file should be in an AI file.

Here is the information that should be included on the label:
1) ingredients:Theobroma Cacao (Cocoa) Seed Butter, Theobroma grandiflorum Ultra Refined Butter, beesewax, Calendula Officinalis Flower Oil, Prunus Amygdalus Dulcis (Sweet Almond) Oil, cetyl alcohol and Tocopherol. Lavandula Angustifolia (Lavender) Oil and Mentha Piperita (Peppermint) Oil.

2) www.kelvorascents.com

3) Brand name and logo: K. Velora Aromatherapy (logo is attached- you can use with form)

```html
<!DOCTYPE html>
<html lang="en">
<head>
<meta charset="utf-8">
<title>K. Velora Aromatherapy – Lavender-Mint Lip Balm Label</title>
<link rel="stylesheet" href="https://fonts.googleapis.com/css2?family=Cormorant+Garamond:wght@500&family=Pathway+Gothic+One&family=Oswald:wght@300&display=swap">
<style>
  :root {
    --page: #ffffff;
    --violet: #6b5fd2;
    --violet-mid: #4b3f99;
    --night: #2a2350;
    --ink: #050408;
    --leaf: #7dba3a;
    --leaf-deep: #5f9a35;
    --lilac: #7b6ee0;
    --lilac-pale: #e1dffb;
    --mist: #ecebff;
    --text-dark: #16141c;
  }
  html, body {
    margin: 0;
    width: 1200px;
    height: 1000px;
    overflow: hidden;
    background: var(--page);
  }
  .label {
    position: absolute;
    left: 345px;
    top: 160px;
    width: 510px;
    height: 680px;
    background: linear-gradient(180deg,
      var(--violet) 0%,
      var(--violet-mid) 12%,
      var(--night) 28%,
      var(--ink) 49%,
      #17132c 60%,
      var(--night) 72%,
      var(--night) 80%,
      var(--violet-mid) 90%,
      var(--violet) 100%);
    overflow: hidden;
  }
  .brand {
    position: absolute;
    left: 16px;
    top: 24px;
    width: 478px;
    height: 108px;
    display: flex;
    align-items: center;
    gap: 16px;
  }
  .brand-dot {
    width: 78px;
    height: 78px;
    border-radius: 50%;
    background: var(--leaf-deep);
    flex: none;
  }
  .brand-name {
    font-family: "Cormorant Garamond", serif;
    font-weight: 500;
    color: var(--leaf);
    margin: 0;
    line-height: 0.9;
  }
  .brand-name .main {
    display: block;
    font-size: 58px;
    letter-spacing: 1px;
  }
  .brand-name .sub {
    display: block;
    font-size: 22px;
    letter-spacing: 3px;
    text-align: right;
    margin-top: 4px;
  }
  .sprigs {
    position: absolute;
    left: 46px;
    top: 160px;
    width: 418px;
    height: 277px;
    background:
      radial-gradient(ellipse 30% 70% at 18% 40%, rgba(167,128,230,0.55), transparent 70%),
      radial-gradient(ellipse 30% 70% at 82% 40%, rgba(167,128,230,0.55), transparent 70%),
      radial-gradient(ellipse 45% 30% at 50% 85%, rgba(140,185,80,0.55), transparent 75%);
  }
  .product {
    position: absolute;
    left: 131px;
    top: 160px;
    width: 249px;
    height: 65px;
    background: #fff;
    border-radius: 14px;
    display: flex;
    align-items: center;
    justify-content: center;
    margin: 0;
    font-family: "Oswald", sans-serif;
    font-weight: 300;
    font-size: 40px;
    color: var(--lilac);
    letter-spacing: -0.5px;
  }
  .ingredients-box {
    position: absolute;
    left: 28px;
    top: 499px;
    width: 455px;
    height: 118px;
    background: var(--lilac-pale);
    border-radius: 17px;
    overflow: hidden;
  }
  .ingredients {
    position: absolute;
    left: 11px;
    top: 7px;
    width: 522px;
    margin: 0;
    transform: scaleX(0.83);
    transform-origin: left top;
    font-family: "Pathway Gothic One", sans-serif;
    font-size: 21px;
    line-height: 26.5px;
    color: var(--text-dark);
  }
  .ingredients .line {
    display: block;
    white-space: nowrap;
    text-align: justify;
    text-align-last: justify;
  }
  .ingredients .line-last {
    text-align-last: left;
  }
  .ingredients .heading {
    color: var(--lilac);
  }
  .site {
    position: absolute;
    left: 0;
    top: 628px;
    width: 510px;
    text-align: center;
    font-family: "Cormorant Garamond", serif;
    font-weight: 500;
    font-size: 31px;
    color: var(--mist);
    margin: 0;
  }
</style>
</head>
<body>
  <main class="label">
    <header class="brand">
      <span class="brand-dot" aria-hidden="true"></span>
      <h1 class="brand-name">
        <span class="main">K. VELORA</span>
        <span class="sub">AROMATHERAPY</span>
      </h1>
    </header>

    <div class="sprigs" role="img" aria-label="Illustrated wreath of lavender sprigs and mint leaves arching around the product name"></div>

    <h2 class="product">LAVENDER-MINT</h2>

    <div class="ingredients-box">
      <p class="ingredients">
        <span class="line"><span class="heading">INGREDIENTS:</span> Theobroma Cacao (Cocoa) Seed Butter, Theobroma</span>
        <span class="line">grandiflorum Ultra Refined Butter, beesewax, Calendula Officinalis Flower Oil,</span>
        <span class="line">Prunus Amygdalus Dulcis (Sweet Almond) Oil, cetyl alcohol and Tocopherol.</span>
        <span class="line line-last">Lavandula Angustifolia (Lavender) Oil and Mentha Piperita (Peppermint) Oil.</span>
      </p>
    </div>

    <p class="site">www.kelvorascents.com</p>
  </main>
</body>
</html>
```